Brand new redesign of Brightwell finance website

I need a new website design that i can advertise a great low interest rate on the front page and capture input application details that will send through to my email address.

some car finance companies will be similar to this would be listed below

quorvaloans.com.au
pelmarfinance.com.au
finance715.com.au
gundrelfinance.com.au
finance93.com.au
Updates

Project Deadline Extended
Reason: I have changed the project to a committed project. all the webpages should have the same format just different content and i want to be able to edit the front page easily to update my interest rates.

Project Deadline Extended
Reason: Provide more time for resubmission and submission work

Target Market(s)

Australian Finance market targeting a younger demographic

Industry/Entity Type

Finance

Coding

Coded - Design and coding required

Number of Pages Required

5+ page

Font styles to use
Serif
Sans Serif

Colors
0255a3
ffffff
cedeed

Requirements
Must have
• application capture form
• apply now buttons
• Headline rate front page

```html
<!DOCTYPE html>
<html lang="en">
<head>
<meta charset="utf-8">
<title>About – Brightwell Finance</title>
<link href="https://fonts.googleapis.com/css2?family=Open+Sans:wght@400;600;700&display=swap" rel="stylesheet">
<style>
:root{
  --blue:#0255a3;
  --navy:#062a55;
  --sky:#0aa3e3;
  --ice:#e4f0f8;
  --nav-bg:#ebeced;
  --text:#2b2b2b;
  --muted:#6a6a6a;
  --foot:#252223;
  --foot-dark:#1c1a1b;
  --white:#ffffff;
}
*{box-sizing:border-box;margin:0;padding:0}
html,body{width:1050px;height:1200px;overflow:hidden;background:var(--white)}
body{font-family:"Open Sans",Arial,sans-serif;color:var(--text);position:relative}
.abs{position:absolute}

.brand{left:141px;top:11px;display:flex;align-items:center;gap:8px}
.brand-dot{width:30px;height:30px;border-radius:50%;background:var(--blue);flex:none}
.brand-name{font-size:18px;line-height:19px;font-weight:700;color:var(--blue);letter-spacing:.5px;text-transform:uppercase;white-space:nowrap}
.callus{left:644px;top:19px;font-size:13.5px;font-weight:600;color:var(--blue)}
.callus b{color:var(--text);font-size:17px;margin-left:4px}
.social-top{left:820px;top:17px;display:flex;gap:9px}
.social-top span{width:24px;height:24px;background:#9a9a9a;display:block}

.nav{left:0;top:63px;width:1050px;height:33px;background:var(--nav-bg)}
.nav ul{list-style:none;position:absolute;left:141px;top:0;display:flex;height:33px}
.nav li{font-size:11px;font-weight:600;text-transform:uppercase;display:flex;align-items:center;justify-content:center;border-right:1px solid #d4d5d6;height:33px;color:#222}
.nav li:last-child{border-right:none}
.nav .apply{background:var(--blue);color:var(--white)}

.hero{left:0;top:96px;width:1050px;height:118px;background:linear-gradient(90deg,#1f6aa6 0%,#2f86be 50%,#4aa7d0 100%);text-align:center;color:var(--white)}
.hero h1{font-size:29px;font-weight:600;margin-top:36px;letter-spacing:.5px}
.hero p{font-size:13.5px;margin-top:4px}

.main{left:142px;width:470px}
.lead{top:263px;font-size:12.3px;font-weight:700;line-height:21px}
.body{font-size:11px;line-height:19px;color:var(--muted)}
.team{left:141px;top:460px;width:472px;height:241px;background:linear-gradient(180deg,#dbe3ea 0%,#8d949c 55%,#3c4148 100%)}
.services{left:142px;top:732px;font-size:26.5px;font-weight:600;color:#2e2e2e}
.checks{left:142px;top:790px;list-style:none}
.checks li{font-size:11px;color:var(--muted);height:26px;display:flex;align-items:flex-start;gap:6px}
.checks svg{margin-top:3px}
.cta{left:142px;top:949px;font-size:12.2px;font-weight:600}
.cta a{color:var(--blue);text-decoration:none}

.phone-box{left:679px;top:267px;width:230px;height:39px;background:var(--ice)}
.phone-icon{position:absolute;left:0;top:0;width:42px;height:39px;background:var(--sky)}
.phone-icon::after{content:"";position:absolute;right:-6px;top:14px;border-left:6px solid var(--sky);border-top:6px solid transparent;border-bottom:6px solid transparent}
.phone-icon svg{position:absolute;left:13px;top:12px}
.phone-box b{position:absolute;left:62px;top:7px;font-size:19px;font-weight:600;color:#222}

.quote{left:679px;top:339px;width:230px;height:287px;background:var(--navy)}
.quote h2{font-size:23px;font-weight:400;color:var(--white);text-align:center;margin-top:18px}
.field{position:absolute;left:17px;width:195px;height:29px;background:var(--white);font-size:9.5px;color:#666;padding-left:10px;display:flex;align-items:center}
.field .caret{position:absolute;right:11px;top:12px;border-top:6px solid #888;border-left:5px solid transparent;border-right:5px solid transparent}
.quote .btn{position:absolute;left:17px;top:231px;width:195px;height:35px;background:var(--sky);color:var(--white);font-size:12px;font-weight:600;display:flex;align-items:center;justify-content:center}

.footer{left:0;top:1016px;width:1050px;height:145px;background:var(--foot);color:var(--white)}
.footer .brand{left:142px;top:45px}
.footer .divider{left:337px;top:49px;width:2px;height:34px;background:var(--sky)}
.footer .about{left:356px;top:41px;width:190px;font-size:10px;line-height:15px}
.footer h3{font-size:12px;font-weight:400;text-transform:uppercase}
.footer .loc{left:597px;top:32px;font-size:9.6px;line-height:15.5px}
.footer .contact{left:761px;top:32px;font-size:9.6px}
.contact p{display:flex;align-items:center;gap:9px;height:20px}
.bottom{left:0;top:1161px;width:1050px;height:39px;background:var(--foot-dark)}
.social-bot{left:142px;top:8px;display:flex;gap:14px}
.social-bot span{width:22px;height:22px;border-radius:50%;background:#2f2c2d;display:block}
.copy{right:141px;top:13px;font-size:9.6px;color:#cfcfcf}
</style>
</head>
<body>

<header>
  <div class="brand abs"><span class="brand-dot"></span><span class="brand-name">Brightwell<br>Finance</span></div>
  <div class="callus abs">Call us: <b>1300-555-274</b></div>
  <div class="social-top abs" aria-label="Social links"><span></span><span></span><span></span></div>
</header>

<nav class="nav abs">
  <ul>
    <li style="width:106px">Home</li>
    <li style="width:109px">About</li>
    <li style="width:118px">Loan&nbsp;
      <svg width="9" height="6" viewBox="0 0 9 6"><path d="M1 1l3.5 3.5L8 1" fill="none" stroke="#333" stroke-width="1.3"/></svg></li>
    <li style="width:173px">Loan Calculator</li>
    <li style="width:125px">Contact</li>
    <li class="apply" style="width:137px">Apply Now</li>
  </ul>
</nav>

<section class="hero abs">
  <h1>ABOUT</h1>
  <p>Get Fast Loan Pre Approval &amp; Apply Online Now</p>
</section>

<main>
  <p class="lead main abs">Duis autem vel eum iriure dolor in hendrerit in vulputate velit esse molestie consequat, vel illum dolore eu feugiat nulla facilisis.</p>
  <p class="body main abs" style="top:321px">Lorem ipsum dolor sit amet, consectetuer adipiscing elit, sed diam nonummy nibh euismod tincidunt ut laoreet dolore magna aliquam erat volutpat. Ut wisi enim ad minim veniam, quis nostrud exerci bortis nisl ut aliquip ex ea commodo consequat.</p>
  <p class="body main abs" style="top:391px">Ut wisi enim ad minim veniam, quis nostrud exerci tation ullamcorper suscipit lobortis nisl ut aliquip ex ea commodo consequat.</p>

  <div class="team abs" role="img" aria-label="Photo of five smiling business people in suits standing together"></div>

  <h2 class="services abs">OUR FINANCIAL SERVICES</h2>
  <ul class="checks abs">
    <li><svg width="11" height="9" viewBox="0 0 11 9"><path d="M1 4.5l3 3L10 1" fill="none" stroke="#0255a3" stroke-width="2"/></svg>Lorem ipsum dolor sit amet, consectetuer adipiscing elit.</li>
    <li><svg width="11" height="9" viewBox="0 0 11 9"><path d="M1 4.5l3 3L10 1" fill="none" stroke="#0255a3" stroke-width="2"/></svg>Duis autem vel eum iriure dolor in hendrerit in vulputate.</li>
    <li><svg width="11" height="9" viewBox="0 0 11 9"><path d="M1 4.5l3 3L10 1" fill="none" stroke="#0255a3" stroke-width="2"/></svg>Delenit augue duis dolore te feugait nulla facilisi.</li>
  </ul>
  <p class="body main abs" style="top:872px">Lorem ipsum dolor sit amet, consectetuer adipiscing elit, sed diam nonummy nibh euismod tincidunt ut laoreet dolore &nbsp;quis nostrud exerci tation ullamcorper suscipit lobortis nisl ut aliquip ex ea commodo consequat.</p>
  <p class="cta abs">To find out more about finance you can <a href="#">Contact Us Online</a> or call <a href="#">1300-555-274</a></p>
</main>

<aside>
  <div class="phone-box abs">
    <div class="phone-icon"><svg width="15" height="15" viewBox="0 0 24 24"><path fill="#fff" d="M6.6 10.8a15.1 15.1 0 0 0 6.6 6.6l2.2-2.2c.3-.3.7-.4 1-.2 1.1.4 2.3.6 3.6.6.6 0 1 .4 1 1V20c0 .6-.4 1-1 1A17 17 0 0 1 3 4c0-.6.4-1 1-1h3.5c.6 0 1 .4 1 1 0 1.3.2 2.5.6 3.6.1.3 0 .7-.2 1z"/></svg></div>
    <b>1300-555-274</b>
  </div>

  <form class="quote abs">
    <h2>Quick Quote</h2>
    <div class="field" style="top:63px">Name *</div>
    <div class="field" style="top:102px">Purpose of Loan *<span class="caret"></span></div>
    <div class="field" style="top:142px">Loan amount *<span class="caret"></span></div>
    <div class="field" style="top:181px">Email *</div>
    <div class="btn">APPLY NOW</div>
  </form>
</aside>

<footer class="footer abs">
  <div class="brand abs"><span class="brand-dot"></span><span class="brand-name">Brightwell<br>Finance</span></div>
  <div class="divider abs"></div>
  <p class="about abs">Lorem ipsum dolor sit amet into ametco consectetuer intoin adipiscing elit, sedip diam nonummy nibh.</p>
  <div class="loc abs">
    <h3>Location</h3>
    <p style="margin-top:12px">Kelvara F 12/308 , 4172<br>Dornau am Felde</p>
  </div>
  <div class="contact abs">
    <h3>Contact Us</h3>
    <div style="margin-top:8px">
      <p><svg width="9" height="9" viewBox="0 0 24 24"><path fill="#777" d="M6.6 10.8a15.1 15.1 0 0 0 6.6 6.6l2.2-2.2c.3-.3.7-.4 1-.2 1.1.4 2.3.6 3.6.6.6 0 1 .4 1 1V20c0 .6-.4 1-1 1A17 17 0 0 1 3 4c0-.6.4-1 1-1h3.5c.6 0 1 .4 1 1 0 1.3.2 2.5.6 3.6.1.3 0 .7-.2 1z"/></svg>1300 555 274</p>
      <p><svg width="9" height="9" viewBox="0 0 10 10"><rect x="1" y="1" width="8" height="8" fill="none" stroke="#777" stroke-width="1.5"/><rect x="3" y="3" width="4" height="2" fill="#777"/></svg>08 9400 3172</p>
      <p><svg width="10" height="8" viewBox="0 0 10 8"><rect width="10" height="8" fill="#777"/><path d="M0 0l5 4 5-4" fill="none" stroke="#252223" stroke-width="1"/></svg>info@brightwellfinance.com</p>
    </div>
  </div>
</footer>

<div class="bottom abs">
  <div class="social-bot abs" aria-label="Social links"><span></span><span></span><span></span></div>
  <p class="copy abs">© 2016, brightwellfinance.com. All rights reserved.</p>
</div>

</body>
</html>
```